I am looking for a modern, clean and neat design for a reflexology and well being business. The business name is Lumen Orto (this is an old Latin word for wellbeing). The colours I would like are purple, white and grey. I am open to suggestions for pictures such as healing or working hands, a pair of feet, images that represent my business that you may think of....... or maybe you think no images at all would be best? My tag line is: "Relax, Renew, Revive" or "Find you balance......... Relax, Renew, Revive" I can decide which I want so I would like to see what both would look like. I would like space on the back to write the client's appointment date and time (more than once)

```html
<!DOCTYPE html>
<html lang="en">
<head>
<meta charset="utf-8">
<title>Lumen Orto – Business Card</title>
<link href="https://fonts.googleapis.com/css2?family=Open+Sans:wght@400;600;700&display=swap" rel="stylesheet">
<style>
  :root {
    --bg: #e7e8ec;
    --card: #ffffff;
    --accent: #a3b8e0;
    --accent-text: #8ba6dc;
    --ink: #3d3f45;
    --ink-soft: #5a5d66;
    --rule: #8a8d96;
  }
  * { margin: 0; padding: 0; box-sizing: border-box; }
  html, body { width: 1200px; height: 900px; overflow: hidden; }
  body {
    background: var(--bg);
    font-family: "Open Sans", Arial, sans-serif;
    color: var(--ink);
    position: relative;
  }
  .card {
    position: absolute;
    left: 250px;
    width: 700px;
    height: 400px;
    background: var(--card);
    border-radius: 30px;
    overflow: hidden;
    box-shadow: 0 6px 20px rgba(0,0,0,0.12);
  }
  .card--back { top: 35px; }
  .card--front { top: 465px; }

  /* Back: appointment side */
  .tagline {
    position: absolute;
    right: 60px;
    top: 70px;
    font-size: 15px;
    font-weight: 600;
    letter-spacing: 0.5px;
    color: var(--ink);
  }
  .brand-mark {
    position: absolute;
    right: 60px;
    top: 108px;
    display: flex;
    align-items: center;
    gap: 12px;
  }
  .brand-mark__dot {
    width: 34px; height: 34px;
    border-radius: 50%;
    background: var(--accent);
  }
  .brand-mark__name {
    font-size: 26px;
    font-weight: 700;
    letter-spacing: 1px;
    color: var(--accent-text);
  }
  .appointment {
    position: absolute;
    left: 60px;
    bottom: 50px;
    width: 400px;
  }
  .appointment__title {
    font-size: 22px;
    font-weight: 700;
    margin-bottom: 14px;
  }
  .appointment__row {
    display: flex;
    align-items: flex-end;
    font-size: 16px;
    color: var(--ink-soft);
    height: 34px;
  }
  .appointment__line {
    flex: 1;
    border-bottom: 2px dotted var(--rule);
    margin-left: 4px;
    margin-bottom: 5px;
  }

  /* Front: contact side */
  .front-circle {
    position: absolute;
    left: 40px;
    top: 175px;
    width: 370px;
    height: 370px;
    border-radius: 50%;
    background: var(--accent);
  }
  .front-brand {
    position: absolute;
    left: 95px;
    top: 300px;
    font-size: 34px;
    font-weight: 600;
    letter-spacing: 1px;
    color: var(--ink);
  }
  .person {
    position: absolute;
    right: 55px;
    top: 120px;
    text-align: right;
    width: 320px;
    border-bottom: 2px solid var(--accent);
    padding-bottom: 4px;
  }
  .person__name {
    font-size: 30px;
    font-weight: 700;
    letter-spacing: 1px;
    color: var(--accent-text);
    line-height: 1.1;
  }
  .person__role {
    font-size: 14px;
    font-weight: 600;
    letter-spacing: 1px;
    color: var(--ink);
  }
  .contacts {
    position: absolute;
    left: 420px;
    top: 230px;
    list-style: none;
    border-top: 2px solid var(--accent);
    padding-top: 8px;
    width: 240px;
  }
  .contacts li {
    display: flex;
    align-items: center;
    gap: 8px;
    font-size: 15px;
    color: var(--accent-text);
    line-height: 24px;
  }
  .contacts svg { width: 13px; height: 13px; flex: none; }
</style>
</head>
<body>

  <section class="card card--back">
    <p class="tagline">RELAX, RENEW, REVIVE</p>
    <div class="brand-mark">
      <span class="brand-mark__dot"></span>
      <span class="brand-mark__name">LUMEN ORTO</span>
    </div>
    <div class="appointment">
      <h2 class="appointment__title">Appointment:</h2>
      <div class="appointment__row">Name:<span class="appointment__line"></span></div>
      <div class="appointment__row">Time:<span class="appointment__line"></span></div>
      <div class="appointment__row">Date:<span class="appointment__line"></span></div>
    </div>
  </section>

  <section class="card card--front">
    <div class="front-circle"></div>
    <p class="front-brand">LUMEN ORTO</p>
    <div class="person">
      <p class="person__name">CLARA VANCE</p>
      <p class="person__role">DIRECTOR</p>
    </div>
    <ul class="contacts">
      <li>
        <svg viewBox="0 0 16 16"><path d="M3 1h3l1.5 4-2 1.5a9 9 0 0 0 4 4L11 8.5l4 1.5v3a2 2 0 0 1-2 2A12 12 0 0 1 1 3a2 2 0 0 1 2-2z" fill="var(--ink)"/></svg>
        +330 5812-3907
      </li>
      <li>
        <svg viewBox="0 0 16 16"><rect x="1.5" y="3.5" width="13" height="9" rx="1" fill="none" stroke="var(--ink)" stroke-width="1.6"/><path d="M2 4l6 5 6-5" fill="none" stroke="var(--ink)" stroke-width="1.6"/></svg>
        info@lumenorto.com
      </li>
      <li>
        <svg viewBox="0 0 16 16"><circle cx="8" cy="8" r="6.5" fill="none" stroke="var(--ink)" stroke-width="1.5"/><path d="M1.5 8h13M8 1.5c-3 3.5-3 9.5 0 13M8 1.5c3 3.5 3 9.5 0 13" fill="none" stroke="var(--ink)" stroke-width="1.2"/></svg>
        www.lumenorto.com
      </li>
    </ul>
  </section>

</body>
</html>
```